Harbor Lane Coaching

We would like to refresh the design of our current website. We want to make it cleaner, more open and more professional looking using simple page layouts and crisp fonts. The site should be lighter and be easy to navigate.

It is important that it be easy to add and change content.

The current site can be seen at www.harborlanecoach.example

As part of this, we want our logo colors to be darker blue and green more professional than they are currently. The current logo is attached as you can see the colors are too "neon"

THIS IS A WEBSITE DESIGN REFRESH PROJECT

Target Market(s)

Executives

Industry/Entity Type

Cleaner

Font styles to use
Sans Serif

Colors
0355a3
cfdfed
9bcb3c

Requirements
Must have
• Ease of use, ease of adding content
Should not have
• No crazy colors, not too busy...

```html
<!DOCTYPE html>
<html lang="en">
<head>
<meta charset="utf-8">
<title>Harbor Lane Coaching</title>
<link rel="stylesheet" href="https://fonts.googleapis.com/css2?family=Open+Sans:wght@400;600&family=Roboto:wght@400;500&family=Raleway:wght@500&family=Noto+Serif:wght@400&display=swap">
<style>
:root{
  --blue:#0355a3;
  --blue-light:#cfdfed;
  --green:#9bcb3c;
  --dark:#2b2e33;
  --footer:#35383d;
  --footer-deep:#25272b;
  --text:#555a60;
  --muted:#8a8f95;
  --white:#ffffff;
  --rule:#d8dce0;
}
*{box-sizing:border-box;margin:0;padding:0}
html,body{width:1200px;height:2364px;overflow:hidden}
body{position:relative;background:var(--white);font-family:"Open Sans",Arial,sans-serif;color:var(--text)}
.abs{position:absolute}

/* hero */
.hero-photo{left:0;top:0;width:1200px;height:606px;background:linear-gradient(120deg,#7d8a95 0%,#b9c3ca 35%,#dde3e7 55%,#a9b3ba 80%,#6f7a83 100%)}
.site-header{left:124px;top:0;width:949px;height:91px;background:var(--white);box-shadow:0 1px 4px rgba(0,0,0,.12)}
.brand{position:absolute;left:6px;top:36px;display:flex;align-items:center;gap:6px;font-family:"Roboto",sans-serif;font-weight:500;font-size:15px;line-height:18px;color:var(--blue);white-space:nowrap}
.brand-mark{width:14px;height:14px;border-radius:50%;background:var(--green);flex:none}
.main-nav{position:absolute;left:190px;top:43px;display:flex;gap:10px;font-family:"Roboto",sans-serif;font-size:11px;line-height:14px;color:#444;text-transform:uppercase;white-space:nowrap}
.contact-mini{position:absolute;left:682px;top:28px;font-size:10px;color:#444;line-height:20px;white-space:nowrap}
.contact-mini div{display:flex;align-items:center;gap:7px}
.members-btn{position:absolute;left:860px;top:34px;width:82px;height:22px;background:var(--blue);color:var(--white);font-size:10.5px;font-weight:600;display:flex;align-items:center;justify-content:center;border-radius:2px;white-space:nowrap}
.hero-title{left:356px;top:209px;width:477px;height:55px;background:rgba(3,85,163,.85);color:var(--white);font-family:"Roboto",sans-serif;font-weight:500;font-size:29px;display:flex;align-items:center;justify-content:center;letter-spacing:.5px}
.hero-sub{left:409px;top:273px;width:355px;height:58px;background:rgba(30,32,36,.88);color:var(--white);font-size:15px;line-height:23px;text-align:center;padding-top:6px}
.btn{display:flex;align-items:center;justify-content:center;color:var(--white);font-family:"Roboto",sans-serif;font-size:14px;text-transform:uppercase;white-space:nowrap}
.btn-register{left:433px;top:411px;width:167px;height:40px;background:#3f8fd6}
.btn-tour{left:609px;top:411px;width:138px;height:40px;background:var(--green)}
.slider-arrow{top:278px;width:36px;height:36px;border-radius:50%;background:#1d1f22}

/* tagline */
.tagline{left:0;top:606px;width:1200px;height:81px;background:#f7f8fa;display:flex;align-items:center;justify-content:center;font-family:"Raleway",sans-serif;font-weight:500;font-size:23px;color:var(--blue)}

/* services */
.services-bg{left:0;top:687px}
.service-title{top:715px;font-family:"Open Sans",sans-serif;font-size:15px;color:#e4e6e8}
.service-photo{top:751px;width:258px;height:182px;border:3px solid var(--white)}

/* clients */
.section-serif{font-family:"Noto Serif",Georgia,serif;color:#222}
.clients-title{left:184px;top:1012px;font-size:23px;letter-spacing:1px}
.clients-rule{left:320px;top:1026px;width:135px;height:2px;background:var(--green)}
.client{width:430px}
.client h3{font-family:"Noto Serif",Georgia,serif;font-weight:400;font-size:15px;color:#222;margin-bottom:18px}
.client p{font-size:12.5px;line-height:19px;color:var(--muted)}
.client a,.read-more{display:block;margin-top:10px;font-size:12.5px;color:var(--blue);text-decoration:none}
.client-icon{width:30px;height:30px}

/* about */
.about-bg{left:0;top:1409px}
.about-head{top:1506px;font-family:"Noto Serif",Georgia,serif;font-size:14px;color:#eef1f4}
.head-rule{height:1px;background:rgba(255,255,255,.8)}
.about-card{left:127px;top:1563px;width:437px;height:331px;background:var(--white);padding:28px 26px;box-shadow:0 2px 8px rgba(0,0,0,.25)}
.about-card p{font-size:12px;line-height:19px;color:var(--muted);margin-bottom:10px}
.tab{left:564px;width:187px;display:flex;align-items:center;justify-content:space-between;padding-left:8px;font-family:"Noto Serif",Georgia,serif;font-size:12px;color:#222}
.tab-active{top:1563px;height:55px;background:var(--white)}
.tab-plain{top:1625px;height:51px;background:#eceef0}
.tab-icon{width:45px;height:100%;display:flex;align-items:center;justify-content:center}
.tab-active .tab-icon{background:var(--blue)}
.ask-list{left:771px;top:1560px;width:250px;font-size:12.5px;line-height:18px;color:#eef1f4}
.ask-list li{list-style:none;padding:8px 0 12px;border-bottom:1px solid rgba(255,255,255,.6);margin-bottom:8px}
.ask-more{color:var(--green);font-size:12.5px}

/* call */
.call-box{left:127px;top:2000px;width:946px;height:114px;background:var(--white);border:1px solid #eceef0;box-shadow:0 1px 3px rgba(0,0,0,.06)}
.call-title{position:absolute;left:32px;top:24px;font-family:"Noto Serif",Georgia,serif;font-weight:400;font-size:27px;color:var(--blue)}
.call-sub{position:absolute;left:32px;top:70px;font-size:13px;color:var(--muted)}
.btn-contact{left:894px;top:2031px;width:155px;height:40px;background:var(--green);border-bottom:3px solid #7fa92c;font-size:14px}

/* footer */
.site-footer{left:0;top:2167px;width:1200px;height:178px;background:var(--footer)}
.footer-bar{left:0;top:2345px;width:1200px;height:19px;background:var(--footer-deep)}
.footer-col{top:2203px;font-size:12px;line-height:20px;color:#c9ccd0}
.footer-col h4{font-family:"Noto Serif",Georgia,serif;font-weight:400;font-size:12px;letter-spacing:1px;color:#e8eaec;margin-bottom:12px}
.social{display:flex;gap:14px;margin-top:12px}
.social span{width:13px;height:13px;border-radius:50%;background:var(--green)}
.field{width:135px;height:14px;border:1px solid #5e6268;background:#2d3034;font-size:8px;line-height:12px;color:#8c9096;padding-left:4px;margin-bottom:3px}
.field-msg{height:26px}
.send{margin-left:85px;width:50px;height:14px;background:#6b6f75;color:#e8eaec;font-size:9px;display:flex;align-items:center;justify-content:center}
</style>
</head>
<body>

<div class="abs hero-photo" role="img" aria-label="Photo of a business presenter speaking to executives around a boardroom table"></div>

<header class="abs site-header">
  <div class="brand"><span class="brand-mark"></span>Harbor Lane Coaching</div>
  <nav class="main-nav">
    <span>Home</span><span>Why Coaching</span><span>About</span><span>Services</span><span>Clients</span><span>Resources</span><span>Contact</span><span>More</span>
  </nav>
  <div class="contact-mini">
    <div><svg width="10" height="10" viewBox="0 0 24 24"><path fill="#555" d="M6.6 10.8a15 15 0 0 0 6.6 6.6l2.2-2.2c.3-.3.7-.4 1-.2 1.1.4 2.3.6 3.6.6.6 0 1 .4 1 1V20c0 .6-.4 1-1 1A17 17 0 0 1 3 4c0-.6.4-1 1-1h3.5c.6 0 1 .4 1 1 0 1.3.2 2.5.6 3.6.1.3 0 .7-.2 1z"/></svg>(555) 210-4830</div>
    <div><svg width="10" height="8" viewBox="0 0 24 18"><rect x="0" y="0" width="24" height="18" fill="#555"/><path d="M0 0l12 9 12-9" fill="none" stroke="#fff" stroke-width="2"/></svg>info@harborlanecoach.example</div>
  </div>
  <div class="members-btn">Members Login</div>
</header>

<div class="abs slider-arrow" style="left:35px"><svg width="36" height="36" viewBox="0 0 36 36"><path d="M20 12l-6 6 6 6" fill="none" stroke="#fff" stroke-width="2.5"/></svg></div>
<div class="abs slider-arrow" style="left:1127px"><svg width="36" height="36" viewBox="0 0 36 36"><path d="M16 12l6 6-6 6" fill="none" stroke="#fff" stroke-width="2.5"/></svg></div>

<h1 class="abs hero-title">FROM DISTRESSED TO SUCCESS</h1>
<p class="abs hero-sub">Harbor Lane Coaching Helps Inspire Individuals<br>Towards Positive and Sustainable Action.</p>
<div class="abs btn btn-register">Register an Account</div>
<div class="abs btn btn-tour">Take a Tour</div>

<h2 class="abs tagline">Leading Is The Way We Help Move People, Including Ourselves, Into Action</h2>

<svg class="abs services-bg" width="1200" height="322" viewBox="0 0 1200 322"><polygon points="0,0 1200,0 1200,273 0,322" fill="#2b2e33"/></svg>
<div class="abs service-title" style="left:162px">Leadership Coaching</div>
<div class="abs service-title" style="left:471px">Assessments</div>
<div class="abs service-title" style="left:782px">Skills Coaching</div>
<div class="abs service-photo" style="left:162px;background:linear-gradient(135deg,#c9b9a4,#7c8ea6 60%,#3a4a63)" role="img" aria-label="Photo of colleagues working at laptops around a table"></div>
<div class="abs service-photo" style="left:471px;background:linear-gradient(135deg,#d7c9c1,#a46a60 55%,#6b2532)" role="img" aria-label="Photo of students writing an assessment"></div>
<div class="abs service-photo" style="left:782px;background:linear-gradient(135deg,#c7b48a,#8c8f8a 50%,#4b5a6c)" role="img" aria-label="Photo of a trainer presenting to a seated group"></div>

<h2 class="abs section-serif clients-title">CLIENTS</h2>
<div class="abs clients-rule"></div>

<svg class="abs client-icon" style="left:132px;top:1066px" viewBox="0 0 30 30"><circle cx="15" cy="8" r="6" fill="#7fb431"/><path d="M4 29c0-8 5-12 11-12s11 4 11 12z" fill="#7fb431"/></svg>
<div class="abs client" style="left:184px;top:1060px">
  <h3>“C” Level Executives</h3>
  <p>For senior executives who want to lead the most powerful, confident and engaged organizations in the world.. Consistently effective leaders create organizations imbued with a “we all win, or no one wins” mentality ...</p>
  <a>Read More</a>
</div>

<svg class="abs client-icon" style="left:624px;top:1066px;width:50px" viewBox="0 0 50 30"><circle cx="10" cy="9" r="5" fill="#7fb431"/><circle cx="25" cy="7" r="6" fill="#7fb431"/><circle cx="40" cy="9" r="5" fill="#7fb431"/><path d="M1 28c0-7 4-10 9-10s9 3 9 10zM15 29c0-8 4-12 10-12s10 4 10 12zM31 28c0-7 4-10 9-10s9 3 9 10z" fill="#7fb431"/></svg>
<div class="abs client" style="left:689px;top:1060px">
  <h3>High Potential Employees</h3>
  <p>Emerging leaders typically earn their status by demonstrating a high level of one tactical skill or another. Unfortunately, they are not always as well equipped with the knowledge and self awareness ...</p>
  <a>Read More</a>
</div>

<svg class="abs client-icon" style="left:132px;top:1244px" viewBox="0 0 30 30"><circle cx="15" cy="8" r="6" fill="#7fb431"/><path d="M4 29c0-8 5-12 11-12s11 4 11 12z" fill="#7fb431"/></svg>
<div class="abs client" style="left:184px;top:1238px">
  <h3>Business Owners and Entrepreneurs</h3>
  <p>Entrepreneurs and business owners are a breed apart. No place in business are outcomes more immediately affected by leadership skill than in this arena. Harbor Lane Coaching’s principals have been in this arena ...</p>
  <a>Read More</a>
</div>

<svg class="abs client-icon" style="left:630px;top:1238px;width:42px;height:40px" viewBox="0 0 42 40"><path d="M22 10l8-8M24 2h6v6" fill="none" stroke="#7fb431" stroke-width="2.5"/><circle cx="12" cy="20" r="5" fill="#7fb431"/><circle cx="29" cy="20" r="5" fill="#7fb431"/><path d="M3 39c0-7 4-10 9-10s9 3 9 10zM20 39c0-7 4-10 9-10s9 3 9 10z" fill="#7fb431"/></svg>
<div class="abs client" style="left:689px;top:1238px">
  <h3>High Potential Youth</h3>
  <p>Teens and young adults are often more open to the possibilities of coaching than their adult counterparts.. Using the Core Leadership Index (CLI) assessment tool in conjunction with the Core Leadership Development System ...</p>
  <a>Read More</a>
</div>

<svg class="abs about-bg" width="1200" height="533" viewBox="0 0 1200 533" role="img" aria-label="Blue-toned photo of a seated audience behind the about section">
  <defs><linearGradient id="aboutTone" x1="0" y1="0" x2="1" y2="1"><stop offset="0" stop-color="#2f4f7c"/><stop offset=".5" stop-color="#3e5f8e"/><stop offset="1" stop-color="#1f3558"/></linearGradient></defs>
  <polygon points="0,46 1200,0 1200,533 0,533" fill="url(#aboutTone)"/>
</svg>

<h2 class="abs about-head" style="left:127px">About Harbor Lane</h2>
<div class="abs head-rule" style="left:302px;top:1517px;width:452px"></div>
<h2 class="abs about-head" style="left:771px">Ask Yourself</h2>
<div class="abs head-rule" style="left:870px;top:1517px;width:206px"></div>

<div class="abs about-card">
  <p>Harbor Lane Coaching works with executives and companies that are facing issues ranging from mild dysfunction to significant distress. We help them pivot, regain control and achieve renewed growth. Harbor Lane Coaching employs the Core Leadership™ process developed by Dana R. Whitfield PhD., founder of the Institute for Applied Coaching Practice (IACP). Core Leadership™ is the process that develops a personally effective style of leadership that positively influences and changes not only the leader, but also those with whom they work and interact, as well as their organization as a whole.</p>
  <p>After 30-years as a senior executive in the print and online business-to-business media business Martin founded Harbor Lane Coaching ...</p>
  <span class="read-more">Read More</span>
</div>

<div class="abs tab tab-active">About Harbor Lane
  <span class="tab-icon"><svg width="18" height="18" viewBox="0 0 24 24"><path d="M3 21l1-5L16 4l4 4L8 20z" fill="#fff"/></svg></span>
</div>
<div class="abs tab tab-plain">Testimonials
  <span class="tab-icon"><svg width="20" height="18" viewBox="0 0 24 22"><path d="M3 3h18v12H10l-5 4v-4H3z" fill="none" stroke="#777" stroke-width="1.6"/></svg></span>
</div>

<ul class="abs ask-list">
  <li>Has my company lost it’s momentum? Is it stuck in neutral or worse?</li>
  <li>Am I frustrated by the lack of cooperation and general apathy among my people?</li>
  <li>Have I lost my edge as a leader? Am I having trouble getting results applying the skills and energy that worked so well in the past?</li>
  <li>Is there a shared vision, do we have a true win-win culture?</li>
  <span class="ask-more">More...</span>
</ul>

<section class="abs call-box">
  <h2 class="call-title">Call T: (555) 210-4830 / F: (555) 210-4831</h2>
  <p class="call-sub">Please contact us to ask questions or to arrange for a complimentary coaching session.</p>
</section>
<div class="abs btn btn-contact">Contact Us</div>

<footer class="abs site-footer"></footer>
<div class="abs footer-bar"></div>
<div class="abs footer-col" style="left:127px">
  <h4>VISIT</h4>
  48 Quayside Road<br>Suite 210-B<br>Milltown, VA 20999
</div>
<div class="abs footer-col" style="left:371px">
  <h4>CONTACT</h4>
  info@harborlanecoach.example
  <div class="social" aria-label="Social links"><span></span><span></span><span></span></div>
</div>
<div class="abs footer-col" style="left:614px">
  <h4>NEWSLETTER</h4>
  <div class="field">Name</div>
  <div class="field">Email</div>
  <div class="field field-msg">Message</div>
  <div class="send">Send</div>
</div>
<div class="abs footer-col" style="left:853px">
  <h4>COPYRIGHT</h4>
  © 2014 by Northgate Works, LLC.
</div>

</body>
</html>
```